Harbor Lights (title of music CD cover)

Create a CD jacket (front and back). Front artwork will be used on CD itself.The CD is an EP (6 songs). They are all love songs (Ballads). Violin, cello, piano, percussion, acoustic guitar, that sort of sound. I am looking for a sophisticated look to the CD. The title is Harbor Lights and the subtitle is The Song of Two. The picture is of me; Lia Brandt. I want this CD jacket to exude class. I have uploaded an example of what i think i want. Obviously rough on my part.

Besides the attached picture of me, I am looking for: my name, name of Cd (Harbor Lights) and subtitle (The Song of Two)
on front of CD

Back:
1. Every Star Grew Quiet (Lia Brandt) 3:26
2. Like Fresh Rain (Lia Brandt) 3:20
3. Once Again Near (Lia Brandt) 4:00
4. The Evening (Lia Brandt) 3:53
5. Here & Always (Lia Brandt) 3:27
6. Harbor Lights (Lia Brandt / Dean Morrow) 4:28
Producer: Dean Morrow
© 2017 Blue Meadow Ventures, LLC

I have some more to go on back: barcode, publishing, additional credits
Updates

Target Market(s)

Adults 25-55

Industry/Entity Type

Music Download

Colors

Designer to choose colors to be used in the design.

Requirements
Must have
• Pic of me on front with title, subtitle and my name

```html
<!DOCTYPE html>
<html lang="en">
<head>
<meta charset="utf-8">
<title>Harbor Lights — CD Jacket</title>
<link rel="stylesheet" href="https://fonts.googleapis.com/css2?family=Tinos:ital@0;1&family=Cormorant+Garamond:wght@500&family=Satisfy&display=swap">
<style>
  :root {
    --ink: #3b3122;
    --ink-soft: #4a3f2e;
    --fog-light: #e6d9bf;
    --fog-mid: #cbb792;
    --fog-deep: #a89472;
    --label-bg: #e7e6e4;
    --portrait-dark: #1c150d;
    --portrait-mid: #6b5234;
    --portrait-warm: #a88a60;
    --scene-grey: #8a8578;
    --glow-outer: #b9a184;
    --glow-inner: #e3d3b8;
    --rule-tan: #c79b70;
    --band-beige: #d8c19d;
    --white: #ffffff;
  }
  * { margin: 0; padding: 0; box-sizing: border-box; }
  html, body { width: 1200px; height: 600px; overflow: hidden; background: #fff; }
  .jacket { position: relative; width: 1200px; height: 600px; display: flex; font-family: "Tinos", "Times New Roman", serif; }

  /* Back cover */
  .back-cover { position: relative; width: 600px; height: 600px; overflow: hidden; }
  .back-scene {
    position: absolute; inset: 0;
    background:
      radial-gradient(ellipse at 70% 45%, rgba(240,230,208,.9), rgba(240,230,208,0) 60%),
      linear-gradient(180deg, var(--fog-mid) 0%, var(--fog-light) 45%, var(--fog-mid) 80%, var(--fog-deep) 100%);
  }
  .tracklist { position: absolute; left: 40px; top: 92px; width: 506px; list-style: none; color: var(--ink); font-size: 21px; }
  .track { display: flex; height: 45.2px; align-items: baseline; white-space: nowrap; }
  .track-no { width: 40px; }
  .track-title { flex: 1; }
  .track-time { text-align: right; }
  .credits { position: absolute; left: 0; width: 600px; text-align: center; font-style: italic; color: var(--ink-soft); font-size: 21px; }
  .credits-main { top: 398px; line-height: 30px; }
  .label-box {
    position: absolute; top: 490px; height: 43px; width: 134px;
    background: var(--label-bg); color: var(--ink);
    font-style: italic; font-size: 21px;
    display: flex; align-items: center; justify-content: center;
  }
  .label-barcode { left: 155px; }
  .label-publishing { left: 301px; }
  .credits-extra { top: 553px; font-size: 20px; }

  /* Front cover */
  .front-cover { position: relative; width: 600px; height: 600px; overflow: hidden; }
  .front-scene {
    position: absolute; inset: 0;
    background:
      linear-gradient(90deg, rgba(28,21,13,0) 0%, rgba(28,21,13,0) 48%, rgba(28,21,13,.55) 54%, rgba(28,21,13,.2) 70%, rgba(28,21,13,.6) 100%),
      radial-gradient(ellipse at 80% 40%, rgba(230,225,212,.7), rgba(230,225,212,0) 55%),
      var(--scene-grey);
  }
  .portrait {
    position: absolute; left: 0; top: 0; width: 330px; height: 600px;
    background:
      radial-gradient(ellipse at 45% 40%, var(--portrait-warm) 0%, var(--portrait-mid) 40%, var(--portrait-dark) 80%),
      var(--portrait-dark);
  }
  .top-band { position: absolute; top: 0; left: 340px; right: 0; height: 8px; background: var(--band-beige); }
  .light-mark { position: absolute; left: 375px; top: 128px; }
  .album-title {
    position: absolute; left: 300px; top: 224px; width: 250px;
    font-family: "Cormorant Garamond", "Times New Roman", serif; font-weight: 500;
    color: var(--white); font-size: 74px; line-height: 66px; text-align: center;
  }
  .title-rule { position: absolute; left: 308px; top: 370px; width: 238px; height: 3px; background: var(--rule-tan); }
  .album-subtitle {
    position: absolute; left: 300px; top: 380px; width: 250px; text-align: center;
    font-family: "Satisfy", cursive; color: var(--white); font-size: 32px; white-space: nowrap;
  }
  .artist-name { position: absolute; right: 32px; top: 540px; color: var(--white); font-size: 31px; }
</style>
</head>
<body>
<main class="jacket">
  <section class="back-cover">
    <div class="back-scene" role="img" aria-label="Misty sepia street with bare trees and an iron fence"></div>
    <ol class="tracklist">
      <li class="track"><span class="track-no">1.</span><span class="track-title">Every Star Grew Quiet (Lia Brandt)</span><span class="track-time">3:26</span></li>
      <li class="track"><span class="track-no">2.</span><span class="track-title">Like Fresh Rain (Lia Brandt)</span><span class="track-time">3:20</span></li>
      <li class="track"><span class="track-no">3.</span><span class="track-title">Once Again Near (Lia Brandt)</span><span class="track-time">4:00</span></li>
      <li class="track"><span class="track-no">4.</span><span class="track-title">The Evening (Lia Brandt)</span><span class="track-time">3:53</span></li>
      <li class="track"><span class="track-no">5.</span><span class="track-title">Here &amp; Always (Lia Brandt)</span><span class="track-time">3:27</span></li>
      <li class="track"><span class="track-no">6.</span><span class="track-title">Harbor Lights (Lia Brandt / Dean Morrow)</span><span class="track-time">4:28</span></li>
    </ol>
    <p class="credits credits-main">Producer: Dean Morrow<br>© 2017 Blue Meadow Ventures, LLC</p>
    <div class="label-box label-barcode">barcode</div>
    <div class="label-box label-publishing">publishing</div>
    <p class="credits credits-extra">additional credits</p>
  </section>

  <section class="front-cover">
    <div class="front-scene" role="img" aria-label="Foggy street with a bare tree and a lamp glow behind the artist"></div>
    <div class="portrait" role="img" aria-label="Sepia portrait of the artist Lia Brandt"></div>
    <div class="top-band"></div>
    <svg class="light-mark" width="80" height="80" viewBox="0 0 80 80" aria-hidden="true">
      <circle cx="40" cy="40" r="38" fill="var(--glow-outer)"/>
      <circle cx="40" cy="40" r="20" fill="var(--glow-inner)"/>
    </svg>
    <h1 class="album-title">Harbor<br>Lights</h1>
    <div class="title-rule"></div>
    <p class="album-subtitle">The Song of Two</p>
    <p class="artist-name">Lia Brandt</p>
  </section>
</main>
</body>
</html>
```